Poem Handwritten by Veteran while in the jungle of Vietnam

My parents are celebrating their 50th wedding anniversary this year. I wanted to give them a very memorable gift. On my parents 2nd anniversary, my father was stationed in Vietnam. On that night he was in the jungle waiting till morning and wrote a poem to my mother using his pant leg as paper. I would like this poem to typographically designed to be framed and hung on the wall.

I have attached a picture of the poem below. It will need to be 11x14 when printed for framing. It would be great if there was background or artwork to make it more visually interesting, perhaps in a watercolor. My parents have a transitional style. I have attached some possible color schemes as well. Cool greens, blue, neutral grays, with hints of berries or highlights of yellow. These are just a guide, I would be open to your interpretations.

Thank you for your help. This will hopefully be a gift they will truly treasure as much as the poem itself.

Target Market(s)

My parents who are excited to be celebrating their 50th wedding anniversary. It should have a transitional, mature style.

Font styles to use
Serif
Script

Requirements
Must have
• The poem, typographically designed. There can be a mix of fonts, but legibility is critically important.
• Now that some designs have come through I wanted to give some more guidance of what I'm looking for. I want something that feels sophisticated and artistic.
Nice to have
• A background or art work, using the color schemes attached as a guide. I am really liking the designs that have a full color landscape artwork in the background. The fonts should be elegant and formal. I really like the romantic, muted colors. I had trouble finding similar projects online in the style I wanted until I cam across wedding invites. Those seem to be the most applicable. I've added pictures of some so you can get a sense of what I'm looking for. I am really liking the jungle foliage, starry skies or sunrises.
Should not have
• Cartoon caricatures, fonts that are too illegible when printed. I'm not liking anything whimsical. I don't like the very bright colors for this project.

```html
<!DOCTYPE html>
<html lang="en">
<head>
<meta charset="utf-8">
<title>Walter's Anniversary Poem</title>
<link rel="stylesheet" href="https://fonts.googleapis.com/css2?family=Dancing+Script:wght@600;700&family=Josefin+Sans:wght@300;400&family=EB+Garamond:ital,wght@0,400;1,400&family=Great+Vibes&display=swap">
<style>
  :root {
    --page-bg: #e4e7ec;
    --sky-top: #1f3552;
    --sky-mid: #4a6280;
    --sunset: #e59a4c;
    --glow: #f6d48e;
    --hills: #6f7f83;
    --grass-light: #a8b95c;
    --grass-dark: #2e4a1c;
    --white: #ffffff;
    --panel: rgba(255, 255, 255, 0.62);
    --title-orange: #e39a3a;
    --ink: #34424f;
    --teal: #2d6f78;
  }
  html, body {
    margin: 0;
    padding: 0;
    width: 1200px;
    height: 1000px;
    overflow: hidden;
    background: var(--page-bg);
  }
  .poster {
    position: absolute;
    left: 227px;
    top: 20px;
    width: 745px;
    height: 960px;
    overflow: hidden;
  }
  .landscape-art {
    position: absolute;
    inset: 0;
    background:
      radial-gradient(ellipse 60% 18% at 78% 44%, var(--glow) 0%, rgba(246,212,142,0) 70%),
      linear-gradient(180deg,
        var(--sky-top) 0%,
        var(--sky-mid) 18%,
        #8a7c7a 30%,
        var(--sunset) 40%,
        #d9b27c 47%,
        var(--hills) 54%,
        var(--grass-light) 62%,
        #6f8a34 78%,
        var(--grass-dark) 100%);
  }
  .title {
    position: absolute;
    left: 0;
    right: 0;
    margin: 0;
    text-align: center;
    color: var(--white);
    font-weight: 400;
  }
  .title-name {
    top: 26px;
    font-family: "Dancing Script", cursive;
    font-weight: 700;
    font-size: 60px;
    line-height: 1;
  }
  .title-occasion {
    top: 94px;
    font-family: "Josefin Sans", sans-serif;
    font-weight: 300;
    font-size: 33px;
    letter-spacing: 4px;
    color: var(--title-orange);
  }
  .title-word {
    top: 122px;
    font-family: "Dancing Script", cursive;
    font-weight: 700;
    font-size: 58px;
    line-height: 1;
  }
  .panel-frame {
    position: absolute;
    inset: 0;
  }
  .poem-column {
    position: absolute;
    top: 236px;
    width: 270px;
    font-family: "EB Garamond", serif;
    font-size: 13.6px;
    line-height: 17.6px;
    color: var(--ink);
    text-align: center;
  }
  .poem-column.left { left: 93px; }
  .poem-column.right { left: 382px; }
  .stanza { margin: 0 0 17.6px; }
  .drop-cap {
    font-family: "Great Vibes", cursive;
    font-size: 34px;
    color: var(--teal);
    line-height: 0;
    vertical-align: -4px;
  }
  .note-rule {
    width: 40px;
    height: 1px;
    background: var(--ink);
    margin: 4px auto 12px;
  }
  .note {
    font-family: "EB Garamond", serif;
    font-style: italic;
    font-size: 8px;
    line-height: 11px;
    margin: 0;
  }
</style>
</head>
<body>
<main class="poster">
  <div class="landscape-art" role="img" aria-label="Sunrise over misty hills and a meadow of tall green grass beneath a deep blue cloudy sky"></div>

  <svg class="panel-frame" width="745" height="960" viewBox="0 0 745 960" aria-hidden="true">
    <polygon points="77,208 379,240 674,208 674,830 77,830" fill="var(--panel)"/>
    <polygon points="77,208 379,240 674,208 674,830 77,830" fill="none" stroke="var(--white)" stroke-width="2"/>
    <polygon points="68,222 362,232 664,200 660,836 72,842" fill="none" stroke="var(--white)" stroke-width="2"/>
  </svg>

  <h1 class="title title-name">Walter's</h1>
  <div class="title title-occasion">ANNIVERSARY</div>
  <div class="title title-word">poem</div>

  <section class="poem-column left">
    <p class="stanza"><span class="drop-cap">L</span>ife's journey began with a challenge,<br>It was heralded far and near.<br>The road led on forever,<br>Its completion was known to be dear.</p>
    <p class="stanza">From the garden of light it proceeded,<br>To the valley of shadows it led.<br>Thorns and thistles adorned it,<br>Past abyss and crevice it sped</p>
    <p class="stanza">The brave surged forward with courage,<br>The wise undaunted pressed on.<br>The mighty held high their banner,<br>We all awaited the dawn.</p>
    <p class="stanza">Though the pitfalls and hazards were many,<br>The pathway was clearly in view.<br>Straight and sure it glided,<br>Its course we knew to be true.</p>
    <p class="stanza">I knew you, Sweetheart, beforehand,<br>So precious and sweet were you.<br>Our moments of bliss were priceless,<br>Each day brought us joy anew.</p>
    <p class="stanza">The call to progression beckoned,<br>At last I would have my chance —<br>To clasp you to me forever,<br>And seal our divine romance.</p>
  </section>

  <section class="poem-column right">
    <p class="stanza">I eagerly started the journey,<br>Though with sorrow, I left you behind.<br>With courage and faith I continued,<br>For I knew, that you later I'd find.</p>
    <p class="stanza">I diligently searched for you, Darling,<br>The roadway was both bleak and fair.<br>Though the years grew long in number,<br>I did not give up in despair.</p>
    <p class="stanza">At last in the distance I saw you,<br>So beautiful, lovely, and sweet!<br>Your attention I struggled to capture,<br>Your love I wrested to meet.</p>
    <p class="stanza">What rapture was mine in fulfillment,<br>As now together we stand,<br>To cherish and love each other,<br>While our plans and dreams expand.</p>
    <p class="stanza">I love you, Darling, forever,<br>My life you have made replete.<br>Our eternal mansion beckons,<br>Your love has made it complete.</p>
    <div class="note-rule"></div>
    <p class="note">This poem was written during the dark of night<br>while on patrol, far from home and loved ones.<br>Penned on a pant leg by lamplight, kept always.<br>The original now rests with our family, a treasure.</p>
  </section>
</main>
</body>
</html>
```